Business Card Design for Mabel's Pantry

We make food for dogs.
Business Card Design (using the logo designed by you). Our Brand color is a bright canary yellow. For example our signage is predominantly yellow, with the logo in black. I'd like the card also to use that imagery.
Feel free to use the two sides creatively.
Vertical Design is also great.

Industry/Entity Type

Pet food

Contact Information for Business Card

Name, email, website, phone no

Font styles to use
Sans Serif

Colors
59FF00
82FF00
B8FF75
E3FFCB
F4FFEA
FFF300
FFF600
FEFA6F
FFFEC7
FFFEE8

Requirements
Nice to have
• A graphic in the same brush stroke style of the logo shoeing a doggy bowl of food

```html
<!DOCTYPE html>
<html lang="en">
<head>
<meta charset="utf-8">
<title>Mabel's Pantry – Business Card</title>
<link rel="stylesheet" href="https://fonts.googleapis.com/css2?family=Oswald:wght@400&family=Barlow+Condensed:wght@400;500;600&display=swap">
<style>
  :root {
    --canvas-bg: #d3d4d6;
    --canary: #ffe155;
    --ink: #151515;
    --paper-white: #ffffff;
  }
  * { margin: 0; padding: 0; box-sizing: border-box; }
  html, body {
    width: 1200px; height: 900px; overflow: hidden;
    background: var(--canvas-bg);
  }
  .canvas { position: relative; width: 1200px; height: 900px; }
  .card {
    position: absolute; top: 115px;
    width: 383px; height: 670px;
    border-radius: 12px;
    overflow: hidden;
    text-align: center;
  }
  .card--front { left: 182px; background: var(--canary); color: var(--ink); }
  .card--back { left: 638px; background: var(--ink); color: var(--paper-white); }

  .wordmark {
    position: absolute; left: 0; right: 0;
    font-family: "Oswald", sans-serif; font-weight: 400;
    text-transform: uppercase; white-space: nowrap; line-height: 1;
  }
  .card--front .wordmark { top: 366px; font-size: 48px; }
  .card--back .wordmark { top: 144px; font-size: 40px; color: var(--canary); }

  .contact {
    position: absolute; left: 0; right: 0;
    font-family: "Barlow Condensed", sans-serif;
    letter-spacing: 0.09em; line-height: 1;
  }
  .owner-name {
    top: 299px; font-size: 28px; font-weight: 600;
    color: var(--canary); letter-spacing: 0.06em;
  }
  .owner-role { top: 336px; font-size: 17px; font-weight: 500; }
  .contact-icons {
    top: 367px; display: flex; justify-content: center; gap: 8px;
  }
  .contact-icons svg { width: 13px; height: 13px; fill: var(--canary); }
  .contact-lines { top: 392px; font-size: 17px; }
  .contact-lines p { height: 23.5px; }
  .pin { top: 474px; }
  .pin svg { width: 14px; height: 20px; fill: var(--canary); }
  .address { top: 508px; font-size: 17px; letter-spacing: 0.04em; }
  .address p { height: 21px; }
  .social {
    top: 600px; font-size: 19px; letter-spacing: 0.03em;
    display: flex; justify-content: center; align-items: center; gap: 6px;
  }
  .social-dot {
    width: 12px; height: 12px; border: 2px solid var(--canary); border-radius: 3px;
  }
</style>
</head>
<body>
<main class="canvas">
  <section class="card card--front" aria-label="Card front">
    <h1 class="wordmark">Mabel's Pantry</h1>
  </section>

  <section class="card card--back" aria-label="Card back">
    <h2 class="wordmark">Mabel's Pantry</h2>
    <p class="contact owner-name">DANA MABEL</p>
    <p class="contact owner-role">Owner</p>
    <div class="contact contact-icons" aria-hidden="true">
      <svg viewBox="0 0 16 16"><path d="M3.5 1l2.5 3-1.5 1.8c.8 1.9 2.3 3.4 4.2 4.2L10.5 8.5l3 2.5-1.2 2.8C7 13.5 2.5 9 2.2 3.7z"/></svg>
      <svg viewBox="0 0 16 16"><path d="M1 3h14v1.2L8 8.8 1 4.2z"/><path d="M1 5.8l7 4.5 7-4.5V13H1z"/></svg>
      <svg viewBox="0 0 16 16"><path d="M8 1a7 7 0 1 0 0 14A7 7 0 0 0 8 1zm0 2c.6.6 1.2 1.8 1.4 3H6.6C6.8 4.8 7.4 3.6 8 3zM3.2 9.4A5 5 0 0 1 3.1 6.6h1.6a11 11 0 0 0 0 2.8zm1.7 1.4h1.8c.2.9.6 1.7 1.1 2.2a5 5 0 0 1-2.9-2.2zM6.6 9.4a9 9 0 0 1 0-2.8h2.8a9 9 0 0 1 0 2.8zm4.7 0a11 11 0 0 0 0-2.8h1.6a5 5 0 0 1-.1 2.8z"/></svg>
    </div>
    <div class="contact contact-lines">
      <p>555-201-4836</p>
      <p>dana@mabelspantry.com</p>
      <p>www.MabelsPantry.com</p>
    </div>
    <div class="contact pin" aria-hidden="true">
      <svg viewBox="0 0 14 20"><path d="M7 0a7 7 0 0 0-7 7c0 5 7 13 7 13s7-8 7-13a7 7 0 0 0-7-7zm0 10a3 3 0 1 1 0-6 3 3 0 0 1 0 6z"/></svg>
    </div>
    <div class="contact address">
      <p>418 W. Linden Ave</p>
      <p>P.O. Box 271</p>
      <p>Harlow, FL 32790</p>
    </div>
    <p class="contact social"><span class="social-dot" aria-hidden="true"></span>mabelspantry</p>
  </section>
</main>
</body>
</html>
```